Holiday Resort Taxi Transfer Website (See Files) - Clean Refresh of Current site.

We would like a refresh of our current website at www.brevolarides.net but we are looking for a BRIGHT, CLEAN YET PROFESSIONAL feel, as we are based in a holiday resort in Spain, but at the same time we want to showcase the fact that our service is HIGH QUALITY and our vehicles are very high standard (see files attached).

We dont provide normal taxis. Our vehicles are almost all Vantorri and are very modern.

Our current colours of blue and white are nice but feel free to change the tones of the colours and add colours if you need to. Light pink may also be very nice.

We want to highlight our booking form at the top of the home page but also highight our reviews as we are top or Wanderscore for our sector/location.

Would be best if you got a feel of the town where we are based by looking at *** www.quillmornpost.com ***

We have a number of websites and the winner will likely get a lot more work as we need refreshes on all.

*Some examples of our competitors are below but we do not particularly like their layouts so please do not copy.
www.kelpomoves.com
www.drivelo-quay.com
www.marbeckshuttles.com
www.portelvinhogroundlinkscoast.com/en
www.belvimonte.com
Updates

After a number of questions i would like to make some of our main points clear that we would like to see on the mockup. 1) The booking form box should be very prominant. 2) Showcase our Wanderscore reviews and the fact that we are Ranked Number 1 on WanderScore for Malaga Airport Transfers. 3) Emphasise our main points below:-a) Pay Driver in Cashb) Free Upgrades from Standard to Luxury. c) No Booking Chargesd) Free Ammendmentse) Free Cancelationf) Door to Door Transfers (not currently emphasised on site) g) Easy booking in under 2 minutes e) No Credit Card Needed. Some other ordinary sites in our sector that we dont want you to copy, but may get ideas from are: http://www.belvimonte.comhttp://www.portelvinhogroundlinkscoast.com/enhttp://www.marbeckshuttles.comhttp://www.drivelo-quay.comhttp://www.kelpomoves.com Added Sunday, August 6, 2017

We have recieved a number of designs which are of low quality. If you do take the time to create a great layout, i can asure you will be in the top 3 and will be guranteed at least €60. But i suspect the one who really reads the project brief well and spends time on the layout will win the contest and along with it a client for serveral more layouts that we need doing. Thank you for your time. Added Monday, August 7, 2017

Target Market(s)

Users who want to book a taxi transfer from Malaga Airport.

Industry/Entity Type

Taxi

Logo Text

Brevola Rides (and Buses by Vendrix)

Number of Pages Required

3 page

Font styles to use
Sans Serif

Colors

Designer to choose colors to be used in the design.

Requirements
Must have
• Must have a BRIGHT/UPLIFTING feel but must be CLEAN, modern and professional at the same time.
• Booking form must be highlighted.
• Our WanderScore rating must be highlighted.
• Our main objectives that are currently listed on the left hand side bar of our current website must be highlighted in a clean way.
Nice to have
• You may wish to use the image of "Brevola" town below. The colours we have at the moment are ok - blue and white - but feel free to use different tones of blue. maybe a lighter shade. We do not like very STRONG colours. The look should be clean bright and uplifiting.
Should not have
• Must not look too formal. We do NOT provide city transfers. We are located in the picturesque town of Brevola on the costa del sol. It is a happy bright holiday resort. We do not want a dull dark look. But we dont want it to look childlike and fun at the same time. It should be bright, clean and uplifting.

```html
<!DOCTYPE html>
<html lang="en">
<head>
<meta charset="utf-8">
<title>Brevola Rides – Airport Transfers</title>
<link rel="stylesheet" href="https://fonts.googleapis.com/css2?family=Open+Sans:ital,wght@0,400;0,600;0,700;0,800;1,400;1,700&display=swap">
<style>
:root{
  --blue:#1592d8;
  --blue-dark:#0f5fa6;
  --navy:#1d4f86;
  --orange:#f9a70b;
  --orange-deep:#f28c0f;
  --ink:#3d3d3d;
  --grey:#555;
  --light:#f3f5f7;
  --white:#fff;
}
*{margin:0;padding:0;box-sizing:border-box}
html,body{width:1200px;height:3381px;overflow:hidden}
body{position:relative;font-family:'Open Sans',sans-serif;color:var(--ink);background:var(--white)}
.abs{position:absolute}
a{color:inherit;text-decoration:none}

/* top bar */
.topbar{left:0;top:0;width:1200px;height:30px;background:var(--blue-dark);color:#fff;font-size:12px}
.topbar .links{left:38px;top:7px;display:flex;gap:14px;align-items:center}
.flag{display:inline-block;width:18px;height:11px;background:#d7e3f2;margin-right:5px;vertical-align:-1px}
.topbar .phone{left:860px;top:0;width:210px;height:30px;background:var(--orange);font-weight:700;font-size:17px;display:flex;align-items:center;justify-content:center;gap:8px}
.topbar .social{left:1085px;top:10px;display:flex;gap:10px}
.topbar .social span{width:10px;height:10px;border-radius:50%;background:#fff}

/* header */
.header{left:0;top:30px;width:1200px;height:108px;background:linear-gradient(#fff,rgba(255,255,255,.85))}
.logo{left:100px;top:52px;display:flex;align-items:center;gap:10px}
.logo i{width:44px;height:44px;border-radius:50%;background:var(--orange)}
.logo b{font-size:30px;font-weight:800;color:var(--blue)}
.logo-tag{left:154px;top:92px;font-size:9px;color:var(--blue)}
.nav{left:488px;top:70px;display:flex;gap:28px;font-size:13px;font-weight:700;color:#444}
.nav .on{color:var(--blue)}

/* hero */
.hero{left:0;top:138px;width:1200px;height:500px;background:linear-gradient(180deg,#8ec6ea 0%,#3f8fcf 30%,#1665b3 60%,#0e4f97 100%)}
.hero-title{left:150px;top:258px;width:482px;text-align:right;color:#fff;font-size:42px;font-weight:700;line-height:1.2}
.btn{display:inline-flex;align-items:center;justify-content:center;background:var(--orange);color:#fff;font-weight:700;font-size:13px;letter-spacing:.5px;transform:skewX(-12deg)}
.btn span{transform:skewX(12deg)}
.hero-btn{left:456px;top:388px;width:164px;height:42px}
.award-shape{left:1098px;top:178px;width:76px;height:76px;border-radius:50%;background:rgba(255,255,255,.9)}
.dots{left:1078px;top:582px;display:flex;gap:7px}
.dots span{width:8px;height:8px;border-radius:50%;background:#fff}
.dots span:first-child{background:var(--orange)}

/* booking */
.booking{left:688px;top:162px;width:305px;height:386px;background:rgba(255,255,255,.95);border:4px solid #c9d6e2;box-shadow:0 6px 20px rgba(0,0,0,.25)}
.booking h2{height:60px;background:var(--orange);font-size:22px;font-weight:700;color:#333;padding:16px 26px}
.booking .field{position:absolute;font-size:11px;color:#999;border-bottom:1px solid #bbb;height:22px;padding-top:2px}
.booking .check{left:28px;top:268px;font-size:11px;color:#777;display:flex;gap:6px;align-items:center}
.booking .check i{width:11px;height:11px;border:1px solid #888}
.booking .show{left:30px;top:300px;width:238px;height:38px;background:var(--blue);color:#fff}
.booking .agent{left:0;top:352px;width:297px;text-align:center;font-size:11px;color:var(--orange-deep)}

/* rated strip */
.rated{left:0;top:638px;width:1200px;height:42px;background:linear-gradient(90deg,#eef1f4,#fff);border-bottom:1px solid #e1e4e8}
.rated p{left:558px;top:9px;font-size:19px;font-weight:700;color:var(--navy)}

/* fleet */
.car{width:192px}
.car .photo{height:124px;background:radial-gradient(ellipse at center,#b8bcc2 0%,#e6e8ea 55%,#fff 75%)}
.car h3{margin-top:32px;height:30px;width:188px;background:var(--blue);color:#fff;font-size:14px;font-weight:700;text-align:center;line-height:30px;transform:skewX(-12deg)}
.car h3 span{display:inline-block;transform:skewX(12deg)}
.car p{margin-top:18px;font-size:13px;line-height:1.75;color:#555}

/* why */
.why-photo{left:0;top:1144px;width:584px;height:358px;background:linear-gradient(135deg,#2c3338 0%,#8f8a86 45%,#d9d3cc 100%)}
.kicker{font-size:14px;font-weight:700;color:var(--blue);letter-spacing:.3px}
.h2{font-size:42px;font-weight:700;color:#555}
.why-text{left:650px;top:1170px;width:360px}
.why-text .h2{margin-top:14px}
.why-text p{margin-top:14px;font-size:14px;line-height:2.15;color:#555}
.why-btn{left:650px;top:1426px;width:187px;height:43px;background:var(--blue)}

/* features */
.feature{width:130px;text-align:center;font-size:14px;font-weight:700;line-height:1.3}
.feature svg{display:block;margin:0 auto 10px;height:58px}
.feature.b{color:var(--blue)}.feature.o{color:var(--orange)}

/* call */
.call{left:0;top:1787px;width:1200px;height:453px;background:linear-gradient(90deg,#f1ede8 0%,#e6ddd2 40%,#b8a591 70%,#d4c3ad 100%)}
.call-kicker{left:162px;top:1896px;color:#222;font-size:16px}
.call-phone{left:160px;top:1915px;font-size:62px;font-weight:700;color:var(--blue-dark);letter-spacing:-1px}
.call-note{left:162px;top:1990px;font-size:16px;font-weight:700;color:#222;line-height:1.5}
.call-btn{left:164px;top:2057px;width:184px;height:42px;background:var(--blue)}

/* reviews */
.award-plain{left:190px;top:2395px;width:170px;height:150px;border-radius:12px;background:#eceff2}
.reviews{left:498px;top:2310px;width:540px}
.reviews .h2{margin-top:6px}
.stars{margin-top:10px;color:var(--orange);font-size:14px;letter-spacing:2px}
.quote{margin-top:4px;font-size:12px;font-style:italic;line-height:2.3;color:#666}
.author{margin-top:16px;font-size:13px;font-weight:700;color:#555}
.author em{color:var(--blue)}
.arrow{font-size:36px;color:#a9d4ef;font-weight:300}

/* chat */
.chat{left:978px;top:2624px;width:222px;height:99px}
.chat .q{height:62px;background:var(--orange-deep);border-radius:12px 0 0 0;padding:8px 16px;color:#333}
.chat .q b{font-size:17px}
.chat .q small{display:block;font-size:8px;font-weight:600;text-align:right}
.chat .s{height:28px;background:#555;color:#fff;font-size:12px;padding:6px 14px}
.chat .s i{display:inline-block;width:9px;height:9px;border-radius:50%;background:#7ed321;margin-right:6px}

/* stats band */
.stats{left:0;top:2723px;width:1200px;height:192px;background:var(--orange)}
.bubble{position:absolute;border-radius:14px;text-align:center;font-weight:700;font-style:italic;display:flex;align-items:center;justify-content:center;line-height:1.25;box-shadow:0 3px 6px rgba(0,0,0,.15)}
.bubble::after{content:"";position:absolute;bottom:-14px;width:0;height:0;border-left:12px solid transparent;border-right:12px solid transparent;border-top:16px solid currentColor}
.bubble.bl{background:#3ea5e0;color:#3ea5e0}.bubble.bl span{color:#fff}
.bubble.wh{background:#fff;color:#fff}.bubble.wh span{color:#333}
.bubble.left::after{left:30px}.bubble.right::after{right:30px}

/* contact */
.contact{left:0;top:2915px;width:1200px;height:401px;background:linear-gradient(180deg,#1a6fbf 0%,#1f7ac8 55%,#2f8ad3 100%)}
.info{display:flex;gap:16px;width:250px}
.info svg{flex:none}
.info h4{font-size:15px;font-weight:700;color:var(--orange)}
.info p{font-size:13px;color:#fff;line-height:1.55}
.inp{position:absolute;background:rgba(255,255,255,.3);color:#fff;font-size:13px;padding:8px 12px}
.submit{left:647px;top:3198px;width:148px;height:38px;background:var(--orange-deep);color:#fff;font-size:13px;font-weight:700;display:flex;align-items:center;justify-content:center}

/* footer */
.footer{left:0;top:3316px;width:1200px;height:65px;background:#fff}
.footer .copy{left:170px;top:22px;font-size:13px;color:#555}
.footer .flinks{left:322px;top:24px;font-size:11px;color:#777;display:flex;gap:8px}
.footer .flinks .on{color:var(--blue)}
.footer .soc{left:932px;top:18px;display:flex;gap:14px}
.footer .soc span{width:24px;height:24px;background:var(--blue-dark)}
.footer .soc span.r{background:#dd4b39}
</style>
</head>
<body>

<div class="abs topbar">
  <div class="abs links"><span><i class="flag"></i>English</span><span>|</span><span>FAQ</span><span>|</span><span>Contact</span><span>|</span><span>✉ bookings@brevolarides.net</span></div>
  <div class="abs phone"><svg width="14" height="14" viewBox="0 0 24 24"><path fill="#fff" d="M6.6 10.8a15 15 0 0 0 6.6 6.6l2.2-2.2a1 1 0 0 1 1-.25 11 11 0 0 0 3.6.6 1 1 0 0 1 1 1V20a1 1 0 0 1-1 1A17 17 0 0 1 3 4a1 1 0 0 1 1-1h3.5a1 1 0 0 1 1 1 11 11 0 0 0 .6 3.6 1 1 0 0 1-.25 1z"/></svg>+34 900 555 012</div>
  <div class="abs social"><span></span><span></span><span></span></div>
</div>

<div class="abs hero" role="img" aria-label="Woman in a sun hat sitting on a rock above the blue Mediterranean coast"></div>
<div class="abs header"></div>
<div class="abs logo"><i></i><b>Brevola Rides</b></div>
<div class="abs logo-tag">and Buses by Vendrix</div>
<nav class="abs nav"><a class="on">Home</a><a>Meeting Point</a><a>Malaga Airport Info</a><a>Prices</a><a>Thanks</a><a>FAQ</a><a>Contact</a></nav>

<h1 class="abs hero-title">Reliable, low cost airport transfers</h1>
<a class="abs btn hero-btn"><span>LEARN MORE ›</span></a>
<div class="abs award-shape" role="img" aria-label="Award badge"></div>
<div class="abs dots"><span></span><span></span><span></span></div>

<form class="abs booking">
  <h2>Book your Taxi</h2>
  <div class="field" style="left:28px;top:80px;width:240px">Pick Up Location</div>
  <div class="field" style="left:28px;top:124px;width:240px">Drop-Off Location</div>
  <div class="field" style="left:28px;top:170px;width:112px">Pick Up Date</div>
  <div class="field" style="left:154px;top:170px;width:114px">Pick Up Time</div>
  <div class="field" style="left:28px;top:216px;width:112px">Adult</div>
  <div class="field" style="left:154px;top:216px;width:114px">Children</div>
  <div class="abs check"><i></i>Round trip transfer</div>
  <a class="abs btn show"><span>SHOW PRICE ›</span></a>
  <div class="abs agent">● Travel Agent Login</div>
</form>

<div class="abs rated"><p class="abs">Rated No.1 on WanderScore</p></div>

<div class="abs car" style="left:151px;top:778px"><div class="photo" role="img" aria-label="Silver saloon car"></div><h3><span>SALOON</span></h3><p>Cum sociis natoque Donec quam felis, ultricies nec, and pellentesque quis eu.</p></div>
<div class="abs car" style="left:388px;top:778px"><div class="photo" role="img" aria-label="Silver station wagon"></div><h3><span>STATION WAGON</span></h3><p>Cum sociis natoque Donec quam felis, ultricies nec, and pellentesque quis eu.</p></div>
<div class="abs car" style="left:625px;top:778px"><div class="photo" role="img" aria-label="Silver eight seat microbus"></div><h3><span>MICROBUS - 8 PAX</span></h3><p>Cum sociis natoque Donec quam felis, ultricies nec, and pellentesque quis eu.</p></div>
<div class="abs car" style="left:857px;top:778px"><div class="photo" role="img" aria-label="Silver twenty seat minibus"></div><h3><span>MINIBUS - 20 PX</span></h3><p>Cum sociis natoque Donec quam felis, ultricies nec, and pellentesque quis eu.</p></div>

<div class="abs why-photo" role="img" aria-label="Smiling driver at the wheel of a car"></div>
<div class="abs why-text">
  <div class="kicker">SHORTLY ABOUT US</div>
  <h2 class="h2">Why Choose Us</h2>
  <p>Lorem ipsum dolor sit amet, consectetur adipisicing elit, sed do eiusmod tempor incididunt ut labore et dolore magna aliqua. Ut enim a corehenderit in cupidatat non proident.</p>
</div>
<a class="abs btn why-btn"><span>KNOW MORE ›</span></a>

<div class="abs feature b" style="left:133px;top:1568px"><svg viewBox="0 0 40 40" width="40"><path d="M30 9a13 13 0 1 0 0 22" fill="none" stroke="#1592d8" stroke-width="4"/><path d="M6 17h18M6 23h18" stroke="#1592d8" stroke-width="3.5"/></svg>Pay Driver<br>in Cash</div>
<div class="abs feature o" style="left:291px;top:1568px"><svg viewBox="0 0 60 40" width="70"><rect x="30" y="4" width="26" height="16" rx="3" fill="#333"/><rect x="4" y="18" width="26" height="14" rx="3" fill="none" stroke="#f9a70b" stroke-width="2"/><circle cx="10" cy="33" r="3" fill="#f9a70b"/><circle cx="24" cy="33" r="3" fill="#f9a70b"/><circle cx="35" cy="21" r="3" fill="#333"/><circle cx="51" cy="21" r="3" fill="#333"/></svg>Free<br>Upgrades</div>
<div class="abs feature o" style="left:461px;top:1568px"><svg viewBox="0 0 40 40" width="40"><path d="M8 8l24 24M32 8L8 32" stroke="#f9a70b" stroke-width="3"/><circle cx="8" cy="32" r="5" fill="none" stroke="#f9a70b" stroke-width="2.5"/><circle cx="32" cy="32" r="5" fill="none" stroke="#f9a70b" stroke-width="2.5"/></svg>Free<br>Cancellation</div>
<div class="abs feature o" style="left:628px;top:1568px"><svg viewBox="0 0 60 40" width="66"><path d="M20 6L4 16l16 10v-6h12v-8H20z" fill="none" stroke="#f9a70b" stroke-width="2.5"/><path d="M40 14l16 10-16 10v-6H28v-8h12z" fill="none" stroke="#f9a70b" stroke-width="2.5"/></svg>Door to Door<br>Transfer</div>
<div class="abs feature o" style="left:797px;top:1568px"><svg viewBox="0 0 40 40" width="40"><rect x="8" y="4" width="26" height="32" rx="3" fill="none" stroke="#f9a70b" stroke-width="2.5"/><circle cx="21" cy="16" r="5" fill="none" stroke="#f9a70b" stroke-width="2.5"/><path d="M13 29a8 8 0 0 1 16 0" fill="none" stroke="#f9a70b" stroke-width="2.5"/><path d="M4 12h6M4 20h6M4 28h6" stroke="#f9a70b" stroke-width="2.5"/></svg>Easy<br>Booking</div>
<div class="abs feature o" style="left:943px;top:1568px"><svg viewBox="0 0 40 40" width="40"><path d="M20 4a11 11 0 0 1 11 11c0 9-11 21-11 21S9 24 9 15A11 11 0 0 1 20 4z" fill="none" stroke="#f9a70b" stroke-width="3"/><circle cx="20" cy="15" r="4" fill="#f9a70b"/></svg>Based in<br>Brevola</div>

<div class="abs call" role="img" aria-label="Smiling couple reading a map in a sunny town street"></div>
<div class="abs kicker call-kicker">CALL US TO BOOK A TAXI</div>
<div class="abs call-phone">+34 900 555 012</div>
<div class="abs call-note">The operator will call back immediately<br>and report the cost of travel</div>
<a class="abs btn call-btn"><span>BOOK TAXI NOW ›</span></a>

<div class="abs award-plain" role="img" aria-label="Ranked number one award badge"></div>
<div class="abs reviews">
  <div class="kicker">RATED NO. 1 ON WANDERSCORE</div>
  <h2 class="h2">See Latest Reviews</h2>
  <div class="stars">★★★★★</div>
  <p class="quote">Whenever I book things blindly on the web it's always a leap of faith. So happy to say that Brevola Rides really delivered exactly as promised. Our driver picked us up in a very comfortable car. He could not have been nicer or more helpful. He recommended a few restaurants and provided some other helpful suggestions to make our stay even better.<br>Overall, great service!</p>
  <p class="author">- Elias on <em>Brevola Rides</em></p>
</div>
<div class="abs arrow" style="left:432px;top:2478px">‹</div>
<div class="abs arrow" style="left:1000px;top:2478px">›</div>

<div class="abs stats">
  <div class="bubble bl left" style="left:158px;top:54px;width:144px;height:86px;font-size:17px"><span>Over 200,000<br>clients driven</span></div>
  <div class="bubble wh left" style="left:300px;top:100px;width:130px;height:58px;font-size:16px"><span>24/7/365<br>service</span></div>
  <div class="bubble bl left" style="left:420px;top:54px;width:122px;height:82px;font-size:16px"><span>Over 50<br>Cars and<br>Minibuses</span></div>
  <div class="bubble wh left" style="left:557px;top:32px;width:201px;height:126px;font-size:22px;font-style:normal"><span style="color:#1592d8">Number 1 on<br>WanderScore</span></div>
  <div class="bubble bl right" style="left:760px;top:80px;width:138px;height:72px;font-size:17px"><span>Cars less than<br>3 years old</span></div>
  <div class="bubble wh right" style="left:902px;top:70px;width:136px;height:88px;font-size:17px"><span>€0 credit<br>card fees</span></div>
</div>

<div class="abs contact" role="img" aria-label="Faint coastal town view behind the contact details"></div>
<div class="abs info" style="left:158px;top:2990px">
  <svg width="44" height="44" viewBox="0 0 44 44"><circle cx="22" cy="22" r="20" fill="none" stroke="#fff" stroke-width="2"/><path d="M22 11a7 7 0 0 1 7 7c0 6-7 14-7 14s-7-8-7-14a7 7 0 0 1 7-7z" fill="none" stroke="#fff" stroke-width="2"/></svg>
  <div><h4>ADDRESS</h4><p>Calle Lorenza 14,<br>Brevola, Malaga, 29781.</p></div>
</div>
<div class="abs info" style="left:384px;top:2990px">
  <svg width="44" height="44" viewBox="0 0 44 44"><circle cx="22" cy="22" r="20" fill="none" stroke="#fff" stroke-width="2"/><rect x="12" y="15" width="20" height="14" fill="none" stroke="#fff" stroke-width="2"/><path d="M12 15l10 8 10-8" fill="none" stroke="#fff" stroke-width="2"/></svg>
  <div><h4>EMAIL</h4><p>bookings@brevolarides.net</p></div>
</div>
<div class="abs info" style="left:158px;top:3090px">
  <svg width="44" height="44" viewBox="0 0 44 44"><circle cx="22" cy="22" r="20" fill="none" stroke="#fff" stroke-width="2"/><path d="M15 13h5l2 6-3 2a12 12 0 0 0 5 5l2-3 6 2v5c-10 1-18-7-17-17z" fill="none" stroke="#fff" stroke-width="2"/></svg>
  <div><h4>PHONE</h4><p>+34 900 555 012</p></div>
</div>
<div class="abs info" style="left:384px;top:3090px">
  <svg width="44" height="44" viewBox="0 0 44 44"><circle cx="22" cy="22" r="20" fill="none" stroke="#fff" stroke-width="2"/><rect x="13" y="18" width="18" height="12" fill="none" stroke="#fff" stroke-width="2"/><rect x="16" y="12" width="12" height="6" fill="none" stroke="#fff" stroke-width="2"/></svg>
  <div><h4>FAX</h4><p>08700 555 019</p></div>
</div>
<div class="abs info" style="left:158px;top:3186px;width:300px">
  <svg width="44" height="44" viewBox="0 0 44 44"><circle cx="22" cy="22" r="20" fill="none" stroke="#fff" stroke-width="2"/><path d="M22 12v10l7 5" fill="none" stroke="#fff" stroke-width="2"/></svg>
  <div><h4>OPENING DAYS:</h4><p>Booking office open every day<br>from: 9:00 to 21:00</p></div>
</div>
<div class="inp" style="left:647px;top:2985px;width:194px;height:38px">Name</div>
<div class="inp" style="left:849px;top:2985px;width:194px;height:38px">Email</div>
<div class="inp" style="left:647px;top:3033px;width:194px;height:38px">Phone Number</div>
<div class="inp" style="left:849px;top:3033px;width:194px;height:38px">Subject</div>
<div class="inp" style="left:647px;top:3081px;width:396px;height:104px">Message</div>
<a class="abs submit">SUBMIT</a>

<div class="abs chat"><div class="q"><b>Question?</b><small>Click here to ask one of our experts</small></div><div class="s"><i></i>Online - Leave a message</div></div>

<footer class="abs footer">
  <div class="abs copy">© 2017 Brevola Rides</div>
  <div class="abs flinks"><span class="on">• Home</span><span>• Meeting Point</span><span>• Malaga Airport Info</span><span>• Prices</span><span>• Thanks</span><span>• FAQ</span><span>• Contact</span></div>
  <div class="abs soc"><span></span><span></span><span class="r"></span></div>
</footer>

</body>
</html>
```